Need Business Card for our Indian Grocery Store

Industry/Entity Type

Grocery Store

Contact Information for Business Card

Manoj Baweja
Director

Store Locations:

Kellbrook
482 Elm Parade
P: 03 9172 5843

Ashvale
613 Carlow Road
P: 03 9238 6014

email: kvtmarts@mailnest.example

Requirements
Must have
• Our logo Colours

```html
<!DOCTYPE html>
<html lang="en">
<head>
<meta charset="utf-8">
<title>KVT Groceries &amp; Spices – Business Card</title>
<link rel="stylesheet" href="https://fonts.googleapis.com/css2?family=Montserrat:wght@400;500;700;800&family=Playfair+Display:ital,wght@1,400&display=swap">
<style>
  :root {
    --brand-blue: #1c1f9e;
    --brand-blue-deep: #0c0f5c;
    --brand-red: #ff1a12;
    --brand-red-deep: #b00600;
    --paper: #ffffff;
    --ink-light: #ffffff;
  }
  * { margin: 0; padding: 0; box-sizing: border-box; }
  html, body { width: 1051px; height: 1200px; overflow: hidden; background: var(--paper); }
  .card-sheet { position: relative; width: 1051px; height: 1200px; font-family: "Montserrat", sans-serif; color: var(--ink-light); }

  .card-front, .card-back { position: absolute; left: 0; width: 1051px; overflow: hidden; }
  .card-front { top: 0; height: 599px; }
  .card-back { top: 603px; height: 597px; }

  .aisle-photo { position: absolute; inset: 0; }
  .card-front .aisle-photo {
    background: radial-gradient(ellipse at 50% 60%, #3a3fd0 0%, var(--brand-blue) 45%, var(--brand-blue-deep) 100%);
  }
  .card-back .aisle-photo {
    background: radial-gradient(ellipse at 50% 55%, #ff4a3a 0%, var(--brand-red) 45%, var(--brand-red-deep) 100%);
  }

  .dashed-frame { position: absolute; left: 43px; width: 970px; }
  .card-front .dashed-frame { top: 43px; height: 519px; border: 2px dashed var(--brand-red); }
  .card-back .dashed-frame { top: 38px; height: 521px; border: 2px dashed var(--ink-light); }

  .centered { position: absolute; left: 0; width: 100%; text-align: center; line-height: 1; white-space: nowrap; }

  .brand-name { top: 150px; font-weight: 800; font-size: 118px; letter-spacing: 6px; }
  .brand-line { top: 300px; font-weight: 800; font-size: 32px; letter-spacing: 3px; }

  .tagline { top: 371px; font-family: "Playfair Display", serif; font-style: italic; font-size: 31px; color: var(--brand-red); letter-spacing: -0.5px; }
  .tagline::before, .tagline::after { content: ""; display: inline-block; width: 44px; height: 2px; background: var(--brand-red); vertical-align: middle; margin: 0 14px; }

  .person-name { top: 448px; font-weight: 800; font-size: 58px; letter-spacing: 4px; }
  .person-role { top: 504px; font-weight: 400; font-size: 22px; letter-spacing: 2px; }

  .chevron { position: absolute; left: 0; top: 0; }

  .locations-heading { top: 80px; font-weight: 400; font-size: 23px; letter-spacing: 2px; line-height: 1.05; white-space: normal; }

  .store-line { font-size: 37px; letter-spacing: 3px; }
  .store-line .suburb { font-weight: 800; }
  .store-line .address { font-weight: 400; }
  .store-first { top: 214px; }
  .store-second { top: 354px; }

  .contact-line { font-size: 33px; font-weight: 400; letter-spacing: 2.5px; display: flex; justify-content: center; align-items: center; gap: 4px; }
  .contact-first { top: 253px; }
  .contact-second { top: 393px; }
  .contact-email { top: 484px; letter-spacing: 1.5px; gap: 8px; }
  .contact-icon { width: 33px; height: 33px; flex: none; }

  .divider { position: absolute; left: 315px; width: 421px; height: 2px; background: var(--ink-light); }
  .divider-one { top: 318px; }
  .divider-two { top: 457px; }
</style>
</head>
<body>
<main class="card-sheet">
  <section class="card-front">
    <div class="aisle-photo" role="img" aria-label="Blue-tinted supermarket aisle with a shopping trolley"></div>
    <div class="dashed-frame"></div>
    <div class="centered brand-name">KVT</div>
    <div class="centered brand-line">GROCERIES &amp; SPICES</div>
    <div class="centered tagline">Trusted Name Since 2011</div>
    <div class="centered person-name">MANOJ BAWEJA</div>
    <div class="centered person-role">DIRECTOR</div>
  </section>

  <section class="card-back">
    <div class="aisle-photo" role="img" aria-label="Red-tinted supermarket aisle with a shopping trolley"></div>
    <svg class="chevron" width="1051" height="200" viewBox="0 0 1051 200" aria-hidden="true">
      <polygon points="138,0 913,0 525,177" fill="var(--brand-blue)"/>
    </svg>
    <div class="dashed-frame"></div>
    <div class="centered locations-heading">STORE<br>LOCATIONS:</div>

    <div class="centered store-line store-first"><span class="suburb">KELLBROOK /</span> <span class="address">482 ELM PARADE</span></div>
    <div class="centered contact-line contact-first">
      <svg class="contact-icon" viewBox="0 0 32 32" aria-hidden="true"><rect width="32" height="32" rx="6" fill="#fff"/><path d="M10 8c1-1 2-1 3 0l2 3c.6 1 .3 1.8-.5 2.5l-1 .8c.8 2 2.3 3.6 4.3 4.4l.8-1c.7-.8 1.6-1 2.5-.5l3 2c1 .7 1 2 0 3l-1.3 1.3c-1.5 1.5-4 1.2-7-1S9.5 17.5 8.3 14.5 7.5 10.5 8.7 9.3z" fill="none" stroke="var(--brand-red)" stroke-width="1.8"/></svg>
      <span>03 9172 5843</span>
    </div>

    <div class="divider divider-one"></div>

    <div class="centered store-line store-second"><span class="suburb">ASHVALE /</span> <span class="address">613 CARLOW ROAD</span></div>
    <div class="centered contact-line contact-second">
      <svg class="contact-icon" viewBox="0 0 32 32" aria-hidden="true"><rect width="32" height="32" rx="6" fill="#fff"/><path d="M10 8c1-1 2-1 3 0l2 3c.6 1 .3 1.8-.5 2.5l-1 .8c.8 2 2.3 3.6 4.3 4.4l.8-1c.7-.8 1.6-1 2.5-.5l3 2c1 .7 1 2 0 3l-1.3 1.3c-1.5 1.5-4 1.2-7-1S9.5 17.5 8.3 14.5 7.5 10.5 8.7 9.3z" fill="none" stroke="var(--brand-red)" stroke-width="1.8"/></svg>
      <span>03 9238 6014</span>
    </div>

    <div class="divider divider-two"></div>

    <div class="centered contact-line contact-email">
      <svg class="contact-icon" viewBox="0 0 32 32" aria-hidden="true"><rect width="32" height="32" rx="6" fill="#fff"/><rect x="6" y="9" width="20" height="14" fill="none" stroke="var(--brand-red)" stroke-width="1.8"/><path d="M6 9l10 8 10-8M6 23l7-7M26 23l-7-7" fill="none" stroke="var(--brand-red)" stroke-width="1.8"/></svg>
      <span>kvtmarts@mailnest.example</span>
    </div>
  </section>
</main>
</body>
</html>
```